We are a specialised ICT Consultancy firm based in Perth, Western Australia. We are looking for an A4 brochure titled “Building Tomorrow Together” that we can use. I have created the content we would like for the brochure in the attachment “Building Tomorrow Together.docx”.
We would like the following on the brochure:
• A copy of the Australian Flag (can be static or rippling in the wind).
• Our logo
• Must be the Meridian blue theme
I have included copies of similar brochures so the designer can get an idea of the theme we are looking for.

```html
<!DOCTYPE html>
<html lang="en">
<head>
<meta charset="utf-8">
<title>Building Tomorrow Together — Meridian Technologies</title>
<link href="https://fonts.googleapis.com/css2?family=Montserrat:ital,wght@0,500;0,800;0,900;1,900&family=Lato:wght@400;700&family=Ubuntu:wght@500;700&display=swap" rel="stylesheet">
<style>
  :root {
    --navy-deep: #0a1650;
    --navy: #13268a;
    --royal: #2440b4;
    --cyan: #26c0f0;
    --white: #ffffff;
    --ink: #17286e;
    --text: #e6ecff;
  }
  * { margin: 0; padding: 0; box-sizing: border-box; }
  html, body { width: 950px; height: 1200px; overflow: hidden; background: var(--navy-deep); }
  .brochure {
    position: relative; width: 950px; height: 1200px; overflow: hidden;
    background: radial-gradient(ellipse at 50% 45%, #2a48bf 0%, #1a3099 45%, #0f1f6d 100%);
    font-family: 'Lato', sans-serif; color: var(--text);
  }
  .top-art, .flag-area, .footer-wave { position: absolute; left: 0; top: 0; }
  .brand {
    position: absolute; left: 52px; top: 120px; display: flex; align-items: center; gap: 10px;
    font-family: 'Montserrat', sans-serif; font-weight: 800; color: var(--ink);
    font-size: 22px; line-height: 1.05; letter-spacing: 1px;
  }
  .brand-square { width: 34px; height: 34px; background: var(--ink); flex: none; }
  .kicker {
    position: absolute; top: 256px; left: 0; width: 950px; text-align: center;
    font-family: 'Montserrat', sans-serif; font-weight: 500; font-size: 25px; color: var(--white);
    letter-spacing: .5px;
  }
  .kicker::before, .kicker::after {
    content: ""; display: inline-block; width: 52px; height: 1px; background: #4d8fe0;
    vertical-align: middle; margin: 0 8px;
  }
  .headline {
    position: absolute; top: 284px; left: 0; width: 950px; text-align: center;
    font-family: 'Montserrat', sans-serif; font-weight: 900; font-size: 86px; line-height: 1;
    color: #f4f6fb; text-shadow: 0 4px 8px rgba(0,0,0,.35); letter-spacing: -1px;
  }
  .tagline-box {
    position: absolute; top: 384px; left: 50%; transform: translateX(-50%);
    border: 2px solid var(--white); border-radius: 16px; padding: 4px 22px;
    display: flex; align-items: center; gap: 12px; white-space: nowrap;
  }
  .tagline-box .star { color: var(--white); font-size: 18px; }
  .tagline-box .word {
    font-family: 'Montserrat', sans-serif; font-style: italic; font-weight: 900;
    font-size: 56px; letter-spacing: 8px; color: var(--cyan); line-height: 1.1;
  }
  .intro {
    position: absolute; top: 474px; left: 70px; width: 810px; text-align: center;
    font-size: 17.5px; line-height: 22px; color: var(--text);
  }
  .hl { color: var(--cyan); font-weight: 700; }
  .section-title {
    font-family: 'Ubuntu', sans-serif; font-weight: 700; line-height: 1.3; color: var(--white);
  }
  .section-title .accent { color: var(--cyan); display: block; }
  .left-block { position: absolute; left: 172px; width: 312px; }
  .left-block .section-title { font-size: 21px; margin-bottom: 10px; }
  .left-block p { font-size: 14.5px; line-height: 18px; margin-bottom: 12px; }
  .challenge { top: 574px; }
  .locally { top: 858px; }
  .icon { position: absolute; }
  .map-panel {
    position: absolute; left: 70px; top: 852px; width: 78px; height: 78px; border-radius: 16px;
    background: linear-gradient(160deg, #2c4cc0, #1a3199); border: 2px solid var(--white);
  }
  .commitment { position: absolute; left: 550px; top: 566px; width: 340px; }
  .commitment .section-title { font-size: 19px; line-height: 1.2; }
  .commitment .section-title .accent { font-size: 26px; line-height: 1.15; margin-top: 6px; }
  .commitment p { font-size: 17px; line-height: 22px; margin-top: 8px; }
  .pillars { position: absolute; left: 543px; top: 730px; width: 340px; list-style: none; }
  .pillar { position: relative; padding-left: 65px; height: 80px; }
  .pillar + .pillar { margin-top: 2px; }
  .pillar::after {
    content: ""; position: absolute; left: 65px; right: 0; bottom: 6px; height: 1px; background: #2a9ee0;
  }
  .pillar:last-child::after { display: none; }
  .pillar svg { position: absolute; left: 0; top: 10px; }
  .pillar h3 {
    font-family: 'Ubuntu', sans-serif; font-weight: 700; font-size: 15px; color: var(--cyan); letter-spacing: .2px;
  }
  .pillar p { font-size: 14.5px; line-height: 18px; margin-top: 3px; }
  .footer {
    position: absolute; left: 0; top: 1050px; width: 950px; height: 150px; text-align: center;
  }
  .footer-note { position: absolute; top: 50px; left: 0; width: 950px; font-size: 17.5px; line-height: 23px; color: var(--text); }
  .footer-link {
    position: absolute; top: 98px; left: 0; width: 950px; font-family: 'Ubuntu', sans-serif;
    font-weight: 700; font-size: 21px; color: var(--cyan);
  }
</style>
</head>
<body>
<main class="brochure">

  <svg class="flag-area" width="950" height="300" role="img" aria-label="Australian flag rippling in the wind">
    <defs>
      <linearGradient id="flagTone" x1="0" y1="0" x2="1" y2="1">
        <stop offset="0" stop-color="#0c1650"/>
        <stop offset=".55" stop-color="#1b2f8c"/>
        <stop offset=".8" stop-color="#3a3f96"/>
        <stop offset="1" stop-color="#5a2f62"/>
      </linearGradient>
    </defs>
    <path d="M240,0 H950 V268 C860,250 760,230 660,226 C560,222 520,190 470,165 C400,130 320,60 240,0 Z" fill="url(#flagTone)"/>
  </svg>

  <svg class="top-art" width="950" height="300" aria-hidden="true">
    <path d="M0,0 H190 C265,35 360,140 510,160 C390,175 260,205 150,250 C95,272 45,282 0,278 Z" fill="#ffffff"/>
    <path d="M0,278 C45,282 95,272 150,250 C260,205 390,175 510,160" fill="none" stroke="#2440b4" stroke-width="5"/>
    <path d="M510,160 C640,190 800,245 950,268" fill="none" stroke="#2a55d0" stroke-width="4" opacity=".7"/>
  </svg>

  <div class="brand">
    <span class="brand-square"></span>
    <span>MERIDIAN<br>TECHNOLOGIES</span>
  </div>

  <div class="kicker">BUILDING</div>
  <h1 class="headline">TOMORROW</h1>
  <div class="tagline-box"><span class="star">★</span><span class="word">TOGETHER</span><span class="star">★</span></div>

  <p class="intro">As a <span class="hl">100% Western Australian-owned</span> ICT provider, Meridian Technologies delivers top-tier tech solutions with a commitment to ethical sourcing that puts Australia first. By partnering with Meridian, you are keeping your investment local and supporting Australia's future.</p>

  <svg class="icon" style="left:58px;top:576px" width="90" height="90" viewBox="0 0 76 76" aria-hidden="true">
    <circle cx="34" cy="34" r="32" fill="#0f1f6d" stroke="#26c0f0" stroke-width="3"/>
    <circle cx="34" cy="34" r="22" fill="none" stroke="#26c0f0" stroke-width="3"/>
    <ellipse cx="34" cy="34" rx="10" ry="22" fill="none" stroke="#26c0f0" stroke-width="3"/>
    <line x1="12" y1="34" x2="56" y2="34" stroke="#26c0f0" stroke-width="3"/>
    <line x1="16" y1="23" x2="52" y2="23" stroke="#26c0f0" stroke-width="2.5"/>
    <line x1="16" y1="45" x2="52" y2="45" stroke="#26c0f0" stroke-width="2.5"/>
    <circle cx="55" cy="55" r="17" fill="#0f1f6d" stroke="#ffffff" stroke-width="3"/>
    <text x="55" y="63" text-anchor="middle" font-family="Ubuntu, sans-serif" font-weight="700" font-size="22" fill="#ffffff">$</text>
  </svg>

  <section class="left-block challenge">
    <h2 class="section-title">THE CHALLENGE OF <span class="accent">BIG TECH TAX AVOIDANCE</span></h2>
    <p>Multinational IT corporations frequently minimise their Australian tax obligations by artificially inflating costs to local subsidiaries. This shifts profits offshore and drastically reduces domestic margins, allowing them to avoid paying their fair share of Australian tax.</p>
    <p>As a local provider, Meridian ensures your ICT spending actively contributes to the Australian tax base and supports national growth.</p>
  </section>

  <div class="map-panel" role="img" aria-label="Outline map of Australia with a tick mark"></div>

  <section class="left-block locally">
    <h2 class="section-title">THE LOCALLY <span class="accent">SOURCED ADVANTAGE</span></h2>
    <p>Meridian is committed to a <span class="hl">100% Australian-owned</span> supply chain. We ensure every dollar spent reinvests directly into our national economy—with all taxes paid straight to the national revenue office.</p>
  </section>

  <section class="commitment">
    <h2 class="section-title">MERIDIAN'S <span class="accent">AUSTRALIAN-FIRST COMMITMENT</span></h2>
    <p>At Meridian, we endeavour to maintain an entirely local supply chain.</p>
  </section>

  <ul class="pillars">
    <li class="pillar">
      <svg width="46" height="46" viewBox="0 0 38 38" aria-hidden="true"><circle cx="19" cy="19" r="17.5" fill="none" stroke="#26c0f0" stroke-width="1.5"/><path d="M9,18 L14,14 L19,17 L24,14 L29,18 L22,25 L16,25 Z" fill="#ffffff"/></svg>
      <h3>DISTRIBUTORS</h3>
      <p>Preferencing Australian-owned supply networks.</p>
    </li>
    <li class="pillar">
      <svg width="46" height="46" viewBox="0 0 38 38" aria-hidden="true"><circle cx="19" cy="19" r="17.5" fill="none" stroke="#26c0f0" stroke-width="1.5"/><path d="M19,15 L14,29 M19,15 L24,29 M15.5,25 H22.5" stroke="#ffffff" stroke-width="1.6" fill="none"/><circle cx="19" cy="14" r="2" fill="#ffffff"/><path d="M14,10 a7,7 0 0 0 0,8 M24,10 a7,7 0 0 1 0,8" stroke="#26c0f0" stroke-width="1.4" fill="none"/></svg>
      <h3>TELECOMMUNICATIONS</h3>
      <p>Partnering with local network and telco providers.</p>
    </li>
    <li class="pillar">
      <svg width="46" height="46" viewBox="0 0 38 38" aria-hidden="true"><circle cx="19" cy="19" r="17.5" fill="none" stroke="#26c0f0" stroke-width="1.5"/><rect x="11" y="11" width="16" height="4.5" rx="1" fill="#ffffff"/><rect x="11" y="17" width="16" height="4.5" rx="1" fill="#ffffff"/><rect x="11" y="23" width="16" height="4.5" rx="1" fill="#ffffff"/></svg>
      <h3>DATA INFRASTRUCTURE</h3>
      <p>Hosting within Australian-owned data centres.</p>
    </li>
    <li class="pillar">
      <svg width="46" height="46" viewBox="0 0 38 38" aria-hidden="true"><circle cx="19" cy="19" r="17.5" fill="none" stroke="#26c0f0" stroke-width="1.5"/><circle cx="19" cy="15" r="3.5" fill="#ffffff"/><circle cx="12" cy="17" r="2.6" fill="#ffffff"/><circle cx="26" cy="17" r="2.6" fill="#ffffff"/><path d="M13,26 a6,6 0 0 1 12,0 Z M7,26 a5,5 0 0 1 7,-5 L13,26 Z M31,26 a5,5 0 0 0 -7,-5 L25,26 Z" fill="#ffffff"/></svg>
      <h3>STRATEGIC PARTNERS</h3>
      <p>Prioritising collaboration with domestic IT vendors</p>
    </li>
  </ul>

  <svg class="footer-wave" style="top:1030px" width="950" height="170" aria-hidden="true">
    <defs>
      <linearGradient id="rim" x1="0" x2="1">
        <stop offset="0" stop-color="#2a55d0"/><stop offset=".5" stop-color="#cfe0ff"/><stop offset="1" stop-color="#2a55d0"/>
      </linearGradient>
    </defs>
    <path d="M0,40 C250,8 700,8 950,40 V170 H0 Z" fill="#0b1852"/>
    <path d="M0,40 C250,8 700,8 950,40" fill="none" stroke="url(#rim)" stroke-width="3"/>
    <path d="M0,60 C150,45 260,42 330,40" fill="none" stroke="#2440b4" stroke-width="6" opacity=".7"/>
    <path d="M620,40 C700,42 800,45 950,60" fill="none" stroke="#2440b4" stroke-width="6" opacity=".7"/>
    <line x1="408" y1="52" x2="452" y2="52" stroke="#26c0f0" stroke-width="1"/>
    <line x1="498" y1="52" x2="542" y2="52" stroke="#26c0f0" stroke-width="1"/>
    <circle cx="475" cy="52" r="12" fill="none" stroke="#26c0f0" stroke-width="1.5"/>
    <circle cx="475" cy="52" r="7" fill="none" stroke="#ffffff" stroke-width="1.2"/>
    <ellipse cx="475" cy="52" rx="3" ry="7" fill="none" stroke="#ffffff" stroke-width="1"/>
    <line x1="468" y1="52" x2="482" y2="52" stroke="#ffffff" stroke-width="1"/>
  </svg>

  <footer class="footer">
    <p class="footer-note">All goods and services provided by Meridian are provided in accordance with<br>our Standard Terms and Conditions available at</p>
    <p class="footer-link">https://www.meridiantechnologies.com.au/t&amp;c</p>
  </footer>

</main>
</body>
</html>
```